2016 Spring tune up

We sell automatic pool covers. We need a postcard design for a mailer to be sent to our customers about a yearly tune up , also offering a discount for a fabric replacement for their automatic pool cover system. The attached information and pictures should be included on the postcard. We would like to see designs that include the colors in our address label

Target Market(s)

Current Automatic Pool Cover Owners

Requirements
Must have
• www.mdrvk.com
• Contact info-service@mdrvk.com
• Attached images and documents
Nice to have
• Color match to our attached logo
Should not have
• Should not have pictures with pools without covers.

```html
<!DOCTYPE html>
<html lang="en">
<head>
<meta charset="utf-8">
<title>2016 Spring Tune Up Postcard</title>
<link rel="stylesheet" href="https://fonts.googleapis.com/css2?family=EB+Garamond:wght@400;600&family=Marcellus&display=swap">
<style>
  :root {
    --backdrop: #2b2b2b;
    --card-pink: #f7d3d4;
    --card-pink-light: #fdf0f0;
    --paper: #ffffff;
    --wine: #6e1d43;
    --wine-bright: #c2347a;
    --rule: #555555;
    --floral-pink: #ee6f95;
    --floral-green: #bcd46a;
    --pool-blue: #2aa7e0;
    --pool-deep: #1170b0;
  }
  * { box-sizing: border-box; margin: 0; padding: 0; }
  html, body { width: 900px; height: 1200px; overflow: hidden; }
  body { background: var(--backdrop); position: relative; }

  .card { position: absolute; left: 115px; width: 670px; height: 516px; overflow: hidden; }

  .card-front {
    top: 68px;
    background: linear-gradient(90deg, var(--card-pink) 0%, var(--card-pink-light) 55%, var(--card-pink) 100%);
  }
  .floral-wreath {
    position: absolute; left: 55px; top: 10px; width: 570px; height: 485px;
    border-radius: 48%;
    background:
      radial-gradient(circle at 25% 30%, rgba(238,111,149,.75) 0 12%, transparent 28%),
      radial-gradient(circle at 78% 28%, rgba(188,212,106,.85) 0 14%, transparent 30%),
      radial-gradient(circle at 85% 62%, rgba(238,111,149,.7) 0 10%, transparent 26%),
      radial-gradient(circle at 18% 70%, rgba(188,212,106,.7) 0 10%, transparent 26%),
      radial-gradient(circle at 50% 50%, rgba(238,200,210,.6) 0 50%, transparent 70%);
  }
  .year-badge {
    position: absolute; left: 167px; top: 152px; width: 332px; height: 332px;
    border-radius: 50%; background: var(--paper);
    display: flex; align-items: center; justify-content: center;
  }
  .year {
    font-family: "Marcellus", serif; font-size: 112px; line-height: 1; letter-spacing: 4px;
    font-variant-numeric: lining-nums;
    background: linear-gradient(180deg, var(--wine) 0%, var(--wine-bright) 55%, var(--wine) 100%);
    -webkit-background-clip: text; background-clip: text; color: transparent;
    margin-top: -4px;
  }

  .card-back { top: 617px; background: var(--paper); }
  .message-panel {
    position: absolute; left: 0; top: 0; width: 463px; height: 100%;
    background: linear-gradient(90deg, var(--card-pink-light) 0%, var(--card-pink) 100%);
  }
  .message {
    position: absolute; left: 25px; top: 22px; width: 412px;
    font-family: "EB Garamond", serif; font-size: 18.6px; line-height: 26.3px; color: var(--wine);
  }
  .message strong { font-weight: 600; }
  .photo { position: absolute; border-radius: 8px; }
  .photo-cover {
    left: 46px; top: 340px; width: 186px; height: 150px; transform: rotate(-4deg);
    background: linear-gradient(180deg, #9c9a8c 0%, var(--pool-blue) 45%, var(--pool-deep) 100%);
  }
  .photo-slats {
    left: 222px; top: 350px; width: 198px; height: 125px; transform: rotate(-6deg);
    background: linear-gradient(135deg, #c9a98e 0%, #c9a98e 25%, #cfdde8 40%, #9ec0d8 100%);
  }
  .stamp-box {
    position: absolute; left: 542px; top: 52px; width: 97px; height: 113px;
    border: 1px solid var(--rule);
  }
  .address-lines { position: absolute; left: 487px; top: 220px; width: 155px; }
  .address-lines span { display: block; height: 1px; background: var(--rule); margin-bottom: 25px; }
</style>
</head>
<body>
  <section class="card card-front">
    <div class="floral-wreath" role="img" aria-label="Illustrated wreath of pink, orange and green flowers and leaves"></div>
    <div class="year-badge"><span class="year">2016</span></div>
  </section>

  <section class="card card-back">
    <div class="message-panel">
      <p class="message">It's time for your 2016 Spring tune up! Before swim season starts, let our service team inspect, clean and adjust your automatic pool cover system so it opens and closes smoothly all summer. Each yearly tune up includes a check of the motor, tracks, ropes and safety settings. Is your cover fabric worn or faded? Book your tune up this spring and save 15% on a fabric replacement for your automatic pool cover. Contact <strong>info-service@mdrvk.com</strong> to reserve your visit, or find details at <strong>www.mdrvk.com</strong></p>
      <div class="photo photo-cover" role="img" aria-label="Photo of an indoor pool with automatic cover track"></div>
      <div class="photo photo-slats" role="img" aria-label="Photo of an automatic pool cover partly closed over the water"></div>
    </div>
    <div class="stamp-box"></div>
    <div class="address-lines"><span></span><span></span><span></span><span></span></div>
  </section>
</body>
</html>
```